Destination Wedding Photographer

I am a Wedding photographer based in San Juan, Puerto Rico. The banner will be shown in the United States to brides that plan to have their wedding in Puerto Rico.

I want to highlight the following words/phrases
Puerto Rico
Destination Wedding
Photographer
(in that order)

feel free to get creative adding your own inspired text.

My web site: www.renzomalvek.com

Target Market(s)

Brides in the united states looking for a photographer for their wedding in Puerto Rico

Industry/Entity Type

Wedding

Requirements
Must have
• + Your ad must be a .gif, .png or .jpg smaller than 40kb in filesize
+ include the following sizes: 300x250, 728x90, 160x600, 468x60, or 120x600
+ Your ad must include the advertiser's brand
+ Your ad must have a border
Should not have
• + Your ad cannot imitate computer effects like scrolling or mousing over
+ No animations longer than 30 seconds
+ No strobe or flashing effects allowed
+ Your ad and campaign must not feature or promote alcohol, anabolic steroids, drugs, financial products, gambling, adult content, or weight loss products

```html
<!DOCTYPE html>
<html lang="en">
<head>
<meta charset="utf-8">
<title>Puerto Rico Destination Wedding Photographer – Banner Set</title>
<link rel="stylesheet" href="https://fonts.googleapis.com/css2?family=Oswald:wght@400;500;700&display=swap">
<style>
  :root{
    --page-bg:#dfe5e1;
    --banner-bg:#2b231d;
    --banner-border:#1a1410;
    --gold-top:#ffd43a;
    --gold-bottom:#f28a00;
    --silver-top:#ffffff;
    --silver-bottom:#a9acb0;
    --photo-green:#6f8f3e;
    --photo-light:#e9ece4;
    --photo-skin:#c99a78;
    --ink:#111111;
    --white:#ffffff;
  }
  *{margin:0;padding:0;box-sizing:border-box}
  html,body{width:1200px;height:818px;overflow:hidden}
  body{background:var(--page-bg);position:relative;font-family:"Oswald",sans-serif}

  .banner{position:absolute;background:var(--banner-bg);border:1px solid var(--banner-border);overflow:hidden}
  .photo{position:absolute;display:block}

  .gold{background:linear-gradient(var(--gold-top),var(--gold-bottom));-webkit-background-clip:text;background-clip:text;color:transparent;font-weight:700;text-transform:uppercase;line-height:1}
  .silver{background:linear-gradient(var(--silver-top) 40%,var(--silver-bottom));-webkit-background-clip:text;background-clip:text;color:transparent;font-weight:700;text-transform:uppercase;line-height:1}
  .stack{position:absolute;text-align:center}
  .stack span{display:block;white-space:nowrap}

  .brand{position:absolute;color:var(--white);font-family:"Oswald",sans-serif;font-weight:400;text-align:center;line-height:1.05;letter-spacing:.5px;white-space:nowrap}

  .cta{position:absolute;display:flex;align-items:center;justify-content:center;gap:6px;border-radius:4px;
       background:linear-gradient(#ffe14a,#f6a400);color:var(--ink);font-weight:500;white-space:nowrap;
       box-shadow:0 1px 0 rgba(255,255,255,.5) inset}
  .cta svg{flex:none}

  /* skyscraper 160x600 */
  .sky{left:32px;top:32px;width:203px;height:761px}
  .sky .stack{left:0;width:203px}
  /* medium rectangle 300x250 */
  .rect{top:157px;width:381px;height:317px}
  .rect-a{left:250px}
  .rect-b{left:651px}
  .rect .stack{left:0;width:176px}
  /* full banner 468x60 */
  .full{left:251px;top:514px;width:594px;height:74px}
  /* leaderboard 728x90 */
  .leader{left:251px;top:606px;width:924px;height:113px}
</style>
</head>
<body>

<!-- skyscraper -->
<div class="banner sky">
  <svg class="photo" style="left:0;top:0" width="203" height="304" viewBox="0 0 203 304" role="img" aria-label="Photo of a bride holding an orange bouquet with the groom in a garden">
    <defs><linearGradient id="skyPhoto" x1="0" y1="0" x2="1" y2="1">
      <stop offset="0" stop-color="var(--photo-green)"/><stop offset=".55" stop-color="var(--photo-skin)"/><stop offset="1" stop-color="var(--photo-light)"/></linearGradient>
      <linearGradient id="skyEdge" x1="0" x2="1"><stop offset="0" stop-color="#888"/><stop offset=".5" stop-color="#fff"/><stop offset="1" stop-color="#777"/></linearGradient></defs>
    <path d="M0,0H203V302Q90,256 0,238Z" fill="url(#skyPhoto)"/>
    <path d="M0,238Q90,256 203,302" fill="none" stroke="url(#skyEdge)" stroke-width="5"/>
  </svg>
  <div class="stack" style="top:312px">
    <span class="gold" style="font-size:54px">Puerto</span>
    <span class="gold" style="font-size:86px;margin-top:2px">Rico</span>
  </div>
  <div class="stack" style="top:478px">
    <span class="silver" style="font-size:36px">Destination</span>
    <span class="silver" style="font-size:46px;margin-top:2px">Wedding</span>
    <span class="silver" style="font-size:26px;margin-top:4px">Photographer</span>
  </div>
  <div class="brand" style="left:0;width:203px;top:640px;font-size:26px">Renzo Malvek<br><span style="font-size:12px;letter-spacing:3px">PHOTOGRAPHY</span></div>
  <div class="cta" style="left:17px;top:710px;width:167px;height:41px;font-size:18px">Learn More!
    <svg width="22" height="22" viewBox="0 0 22 22" aria-hidden="true"><circle cx="11" cy="11" r="11" fill="var(--ink)"/><path d="M9 6l5 5-5 5" fill="none" stroke="var(--white)" stroke-width="2.6"/></svg></div>
</div>

<!-- medium rectangles -->
<div class="banner rect rect-a">
  <svg class="photo" style="left:0;top:0" width="381" height="317" viewBox="0 0 381 317" role="img" aria-label="Photo of the bride and groom smiling at each other, bride holding an orange bouquet">
    <defs><linearGradient id="rectPhotoA" x1="0" y1="0" x2="1" y2="1">
      <stop offset="0" stop-color="var(--photo-skin)"/><stop offset=".5" stop-color="var(--photo-light)"/><stop offset="1" stop-color="var(--photo-green)"/></linearGradient></defs>
    <path d="M195,0H381V317H215Q168,170 195,0Z" fill="url(#rectPhotoA)"/>
    <path d="M195,0Q168,170 215,317" fill="none" stroke="#d8d8d8" stroke-width="5"/>
  </svg>
  <div class="stack" style="top:10px"><span class="gold" style="font-size:42px">Puerto</span><span class="gold" style="font-size:72px">Rico</span></div>
  <div class="stack" style="top:140px"><span class="silver" style="font-size:28px">Destination</span><span class="silver" style="font-size:38px">Wedding</span><span class="silver" style="font-size:23px;margin-top:2px">Photographer</span></div>
  <div class="brand" style="left:0;width:176px;top:256px;font-size:22px">Renzo Malvek<br><span style="font-size:10px;letter-spacing:3px">PHOTOGRAPHY</span></div>
  <div class="cta" style="left:198px;top:269px;width:159px;height:39px;font-size:17px">Learn More!
    <svg width="20" height="20" viewBox="0 0 22 22" aria-hidden="true"><circle cx="11" cy="11" r="11" fill="var(--ink)"/><path d="M9 6l5 5-5 5" fill="none" stroke="var(--white)" stroke-width="2.6"/></svg></div>
</div>

<div class="banner rect rect-b">
  <svg class="photo" style="left:0;top:0" width="381" height="317" viewBox="0 0 381 317" role="img" aria-label="Photo of the bride and groom smiling at each other, bride holding an orange bouquet">
    <defs><linearGradient id="rectPhotoB" x1="0" y1="0" x2="1" y2="1">
      <stop offset="0" stop-color="var(--photo-skin)"/><stop offset=".5" stop-color="var(--photo-light)"/><stop offset="1" stop-color="var(--photo-green)"/></linearGradient></defs>
    <path d="M195,0H381V317H215Q168,170 195,0Z" fill="url(#rectPhotoB)"/>
    <path d="M195,0Q168,170 215,317" fill="none" stroke="#d8d8d8" stroke-width="5"/>
  </svg>
  <div class="stack" style="top:10px"><span class="gold" style="font-size:42px">Puerto</span><span class="gold" style="font-size:72px">Rico</span></div>
  <div class="stack" style="top:140px"><span class="silver" style="font-size:28px">Destination</span><span class="silver" style="font-size:38px">Wedding</span><span class="silver" style="font-size:23px;margin-top:2px">Photographer</span></div>
  <div class="brand" style="left:0;width:176px;top:256px;font-size:22px">Renzo Malvek<br><span style="font-size:10px;letter-spacing:3px">PHOTOGRAPHY</span></div>
  <div class="cta" style="left:198px;top:269px;width:159px;height:39px;font-size:17px">Learn More!
    <svg width="20" height="20" viewBox="0 0 22 22" aria-hidden="true"><circle cx="11" cy="11" r="11" fill="var(--ink)"/><path d="M9 6l5 5-5 5" fill="none" stroke="var(--white)" stroke-width="2.6"/></svg></div>
</div>

<!-- full banner -->
<div class="banner full">
  <svg class="photo" style="left:0;top:0" width="205" height="74" viewBox="0 0 205 74" role="img" aria-label="Photo of the bride and groom with a flowing veil in a garden">
    <defs><linearGradient id="fullPhoto" x1="0" x2="1"><stop offset="0" stop-color="var(--photo-green)"/><stop offset=".45" stop-color="var(--photo-skin)"/><stop offset="1" stop-color="var(--photo-light)"/></linearGradient></defs>
    <path d="M0,0H199L186,74H0Z" fill="url(#fullPhoto)"/><path d="M199,0L186,74" stroke="#ccc" stroke-width="4"/>
  </svg>
  <div class="stack" style="left:205px;width:274px;top:3px"><span class="gold" style="font-size:38px">Puerto Rico</span><span class="silver" style="font-size:15px;margin-top:4px">Destination Wedding Photographer</span></div>
  <div class="brand" style="left:484px;width:100px;top:6px;font-size:15px">Renzo Malvek<br><span style="font-size:7px;letter-spacing:2px">PHOTOGRAPHY</span></div>
  <div class="cta" style="left:489px;top:45px;width:95px;height:23px;font-size:12px;gap:4px">Learn More!
    <svg width="13" height="13" viewBox="0 0 22 22" aria-hidden="true"><circle cx="11" cy="11" r="11" fill="var(--ink)"/><path d="M9 6l5 5-5 5" fill="none" stroke="var(--white)" stroke-width="2.6"/></svg></div>
</div>

<!-- leaderboard -->
<div class="banner leader">
  <svg class="photo" style="left:0;top:0" width="310" height="113" viewBox="0 0 310 113" role="img" aria-label="Photo of the groom and bride smiling, her veil flowing behind in a garden">
    <defs><linearGradient id="leaderPhoto" x1="0" x2="1"><stop offset="0" stop-color="var(--photo-green)"/><stop offset=".45" stop-color="var(--photo-skin)"/><stop offset="1" stop-color="var(--photo-light)"/></linearGradient></defs>
    <path d="M0,0H307L290,113H0Z" fill="url(#leaderPhoto)"/><path d="M307,0L290,113" stroke="#ccc" stroke-width="5"/>
  </svg>
  <div class="stack" style="left:313px;width:440px;top:8px"><span class="gold" style="font-size:59px">Puerto Rico</span><span class="silver" style="font-size:25px;margin-top:7px">Destination Wedding Photographer</span></div>
  <div class="brand" style="left:760px;width:150px;top:8px;font-size:24px">Renzo Malvek<br><span style="font-size:10px;letter-spacing:3px">PHOTOGRAPHY</span></div>
  <div class="cta" style="left:762px;top:67px;width:146px;height:37px;font-size:17px">Learn More!
    <svg width="20" height="20" viewBox="0 0 22 22" aria-hidden="true"><circle cx="11" cy="11" r="11" fill="var(--ink)"/><path d="M9 6l5 5-5 5" fill="none" stroke="var(--white)" stroke-width="2.6"/></svg></div>
</div>

</body>
</html>
```